Clean bold and classy business card front and back
Rin can be the logo
My name Dorian Hesketh as owner
Phone email and address
Owner Dorian Hesketh
Phone 8505550147
Email ridgelineinsulate@mailbox.test
Address170 frank pais rd Havana fl 32390

Industry/Entity Type

Business

Contact Information for Business Card

Owner Dorian Hesketh
Phone 8505550147

Requirements
Must have
• Ridgeline insulate co under Rin logo
Nice to have
• Bold and clean. Maybe use Rin as logo and name under it. Have logo on one side and info on the other side with logo also
• Put a pic up. It doesn't have to be that but something that can be used
• Try some fancy fonts also

```html
<!DOCTYPE html>
<html lang="en">
<head>
<meta charset="utf-8">
<title>Ridgeline Insulate Co — Business Card</title>
<link href="https://fonts.googleapis.com/css2?family=Montserrat:wght@400;500;700;800&display=swap" rel="stylesheet">
<style>
  :root {
    --page-bg: #ecebe8;
    --card-white: #ffffff;
    --brand-blue: #2f7fc1;
    --brand-orange: #f08a24;
    --back-blue: #3f87c7;
    --back-blue-deep: #2e72b0;
    --back-blue-light: #5c9ad2;
    --ink: #1d1d1d;
    --on-blue: #ffffff;
  }
  * { margin: 0; padding: 0; box-sizing: border-box; }
  html, body {
    width: 1200px;
    height: 1000px;
    overflow: hidden;
    background: var(--page-bg);
    font-family: "Montserrat", sans-serif;
  }
  .card {
    position: absolute;
    left: 265px;
    width: 665px;
    height: 397px;
    border-radius: 24px;
    overflow: hidden;
    box-shadow: 0 4px 14px rgba(0,0,0,0.18);
  }
  .card--front { top: 73px; background: var(--card-white); }
  .card--back { top: 532px; background: var(--back-blue); }

  .brand {
    position: absolute;
    left: 0;
    width: 100%;
    text-align: center;
    font-family: "Montserrat", sans-serif;
    font-weight: 800;
  }
  .brand__mark {
    display: flex;
    justify-content: center;
    align-items: center;
    gap: 16px;
    font-size: 84px;
    line-height: 1;
    letter-spacing: 1px;
  }
  .brand__square {
    width: 26px;
    height: 26px;
  }
  .brand__name {
    margin-top: 22px;
    font-size: 33px;
    line-height: 1;
  }
  .card--front .brand { top: 52px; }
  .card--front .brand__mark { color: var(--brand-orange); }
  .card--front .brand__square { background: var(--brand-blue); }
  .card--front .brand__name { color: var(--brand-blue); }

  .card--back .brand { top: 112px; }
  .card--back .brand__mark,
  .card--back .brand__name { color: var(--on-blue); }
  .card--back .brand__square { background: var(--on-blue); }

  .back-photo {
    position: absolute;
    inset: 0;
    background:
      radial-gradient(ellipse at 22% 35%, var(--back-blue-light) 0%, transparent 45%),
      radial-gradient(ellipse at 80% 70%, var(--back-blue-deep) 0%, transparent 55%),
      linear-gradient(135deg, var(--back-blue-deep), var(--back-blue) 50%, var(--back-blue-light));
    opacity: 0.85;
  }

  .contact {
    position: absolute;
    top: 248px;
    left: 0;
    width: 100%;
    text-align: center;
    color: var(--ink);
  }
  .contact__name {
    font-size: 19px;
    font-weight: 700;
    letter-spacing: 0.5px;
    line-height: 1;
  }
  .contact__role {
    display: flex;
    justify-content: center;
    align-items: center;
    gap: 8px;
    margin-top: 4px;
    color: var(--brand-orange);
    font-size: 13.5px;
    font-weight: 500;
  }
  .contact__rule {
    width: 66px;
    height: 1.5px;
    background: var(--brand-orange);
  }
  .contact__line {
    font-size: 15px;
    font-weight: 400;
    line-height: 23px;
  }
  .contact__phone { margin-top: 14px; }
  .contact__address { letter-spacing: 2px; margin-top: 3px; }
</style>
</head>
<body>

  <section class="card card--front">
    <div class="brand">
      <div class="brand__mark"><span class="brand__square"></span>Rin</div>
      <div class="brand__name">Ridgeline insulate co</div>
    </div>
    <div class="contact">
      <div class="contact__name">DORIAN HESKETH</div>
      <div class="contact__role"><span class="contact__rule"></span>Owner<span class="contact__rule"></span></div>
      <div class="contact__line contact__phone">8505550147</div>
      <div class="contact__line">ridgelineinsulate@mailbox.test</div>
      <div class="contact__line contact__address">482 tilden oak rd Havana fl 32390</div>
    </div>
  </section>

  <section class="card card--back">
    <div class="back-photo" role="img" aria-label="Blue-tinted photo of an installer in protective gear spraying foam insulation"></div>
    <div class="brand">
      <div class="brand__mark"><span class="brand__square"></span>Rin</div>
      <div class="brand__name">Ridgeline insulate co</div>
    </div>
  </section>

</body>
</html>
```